Youtube Thumbnail templates x 4 for football channel (more than 1 winner will be chosen)

I am looking for a set of 4 thumbnail templates that are on brand.

They should be eye catching and baiting the click.

The 4 different thumbnails will likely be very similar.

It is highly likely that I will choose more than 1 designer as the winner for the project

I have added my brand guidelines below as well as my logo.

The website page to get a good feel for my brand is: https://brightpitch.example/434-coaching/

Also, please feel free to add any images of famous footballers in the template, as these will be delivered in PSD file at the end I will be able to edit these thumbnails before they go live

Target Market(s)

Football players of all levels

Font styles to use
Sans Serif

Requirements
Must have
• Be on brand.
Be eye catching and very clickable

```html
<!DOCTYPE html>
<html lang="en">
<head>
<meta charset="utf-8">
<title>Marco Castellos – Thumbnail</title>
<link rel="stylesheet" href="https://fonts.googleapis.com/css2?family=Anton&display=swap">
<style>
  :root {
    --red-deep: #8e0000;
    --red: #c40a0a;
    --red-bright: #e01515;
    --stadium-grey: #6e6464;
    --stadium-dark: #3d3535;
    --white: #ffffff;
    --glow: rgba(255, 255, 255, 0.75);
  }
  html, body {
    margin: 0;
    padding: 0;
    width: 1200px;
    height: 675px;
    overflow: hidden;
    background: var(--red-deep);
  }
  .thumbnail {
    position: relative;
    width: 1200px;
    height: 675px;
    overflow: hidden;
    background: linear-gradient(180deg, var(--red-deep) 0%, var(--red) 55%, var(--red-bright) 100%);
    font-family: "Anton", "Impact", sans-serif;
  }
  .stadium-backdrop {
    position: absolute;
    inset: 0;
    background: linear-gradient(180deg, var(--stadium-dark) 0%, var(--stadium-grey) 18%, #7b6262 30%, rgba(150, 30, 30, 0.6) 48%, rgba(180, 10, 10, 0) 70%);
  }
  .player-photo {
    position: absolute;
    left: 205px;
    top: 0;
    width: 600px;
    height: 675px;
    border-radius: 280px 280px 0 0;
    background: linear-gradient(180deg, #5a5252 0%, #7a6e6e 22%, #d81e1e 40%, #e42222 75%, #b80d0d 100%);
  }
  .player-name {
    position: absolute;
    inset: 0;
    width: 1200px;
    height: 675px;
  }
  .player-name text {
    font-family: "Anton", "Impact", sans-serif;
    fill: var(--white);
    filter: drop-shadow(0 0 10px var(--glow));
  }
  .player-name .outlined {
    fill: none;
    stroke: var(--white);
    stroke-width: 2;
  }
  .brand {
    position: absolute;
    right: 42px;
    bottom: 32px;
    display: flex;
    align-items: center;
    gap: 10px;
    color: var(--white);
  }
  .brand-mark {
    width: 56px;
    height: 56px;
    border-radius: 50%;
    background: var(--white);
  }
  .brand-name {
    font-family: "Anton", "Impact", sans-serif;
    font-size: 24px;
    line-height: 0.95;
    letter-spacing: 0.5px;
    text-transform: uppercase;
  }
</style>
</head>
<body>
  <main class="thumbnail">
    <div class="stadium-backdrop" role="img" aria-label="Black and white stadium stand and roof fading into a red backdrop with floating orange sparks"></div>
    <div class="player-photo" role="img" aria-label="Cut-out photo of a midfielder in a red home shirt pointing to the left"></div>

    <svg class="player-name" viewBox="0 0 1200 675" aria-label="Marco Castellos">
      <text x="590" y="258" font-size="180" textLength="470" lengthAdjust="spacingAndGlyphs">MARCO</text>
      <text x="180" y="462" font-size="262" textLength="810" lengthAdjust="spacingAndGlyphs">CAS<tspan class="outlined">TEL</tspan>LOS</text>
    </svg>

    <div class="brand">
      <div class="brand-mark"></div>
      <div class="brand-name">Bold<br>Striker</div>
    </div>
  </main>
</body>
</html>
```